Bref créative
The Lanternwrights
We make it work, always!
Professional
Rosalind Kettering
Partner
48 Thornapple Lane
Marlowe Springs, OH 45871
rosalind.k.kettering@thelanternwrights.net
www.thelanternwrights.net
logo will be attached
second set of business cards needed
Dean Oltveld
dean.oltveld@thelanternwrights.net
Your Trusted Advisors
Updated logo in CMYK format

```html
<!DOCTYPE html>
<html lang="en">
<head>
<meta charset="utf-8">
<title>The Lanternwrights – Business Cards</title>
<link href="https://fonts.googleapis.com/css2?family=Open+Sans:wght@400;600;700;800&display=swap" rel="stylesheet">
<style>
  :root {
    --backdrop: #c89b6d;
    --card-top: #ffffff;
    --card-bottom: #e2e3e5;
    --ink: #222222;
    --ink-soft: #3a3a3a;
    --accent-red: #e3332a;
    --brand-blue: #1f2f5c;
    --mark: #e8532c;
  }
  * { margin: 0; padding: 0; box-sizing: border-box; }
  html, body {
    width: 1200px; height: 538px; overflow: hidden;
    background: var(--backdrop);
    font-family: "Open Sans", Arial, sans-serif;
  }
  .stage { position: relative; width: 1200px; height: 538px; }
  .card {
    position: absolute; top: 108px;
    width: 530px; height: 384px;
    border-radius: 24px;
    background: linear-gradient(180deg, var(--card-top) 0%, var(--card-bottom) 100%);
    box-shadow: 0 6px 14px rgba(0,0,0,0.28);
  }
  .card--front { left: 56px; }
  .card--back { left: 626px; }

  .brand-mark { position: absolute; border-radius: 50%; background: var(--mark); }
  .card--front .brand-mark { left: 52px; top: 52px; width: 98px; height: 98px; }
  .brand-name {
    position: absolute; left: 20px; top: 150px;
    font-weight: 800; font-size: 26px; letter-spacing: -0.4px; line-height: 1;
    color: var(--brand-blue); text-transform: uppercase;
  }
  .brand-tagline {
    position: absolute; left: 22px; top: 178px;
    font-weight: 700; font-size: 12px; letter-spacing: 0.3px; line-height: 1;
    color: var(--accent-red); text-transform: uppercase;
  }

  .holder { position: absolute; right: 62px; top: 118px; text-align: right; }
  .holder__name { font-weight: 700; font-size: 14px; line-height: 1.2; color: var(--ink); text-transform: uppercase; }
  .holder__role { font-weight: 600; font-size: 9px; color: var(--accent-red); text-transform: uppercase; margin-top: 2px; }

  .contact {
    position: absolute; right: 62px; top: 242px;
    font-style: normal; text-align: right;
    font-size: 10.5px; line-height: 19px; color: var(--ink-soft);
    white-space: nowrap;
  }

  .card--back .brand-mark { left: 66px; top: 44px; width: 148px; height: 148px; }
  .web {
    position: absolute; right: 44px; top: 244px;
    font-weight: 700; font-size: 17px; color: var(--ink); text-transform: uppercase;
    white-space: nowrap;
  }
</style>
</head>
<body>
<main class="stage">
  <section class="card card--front">
    <div class="brand-mark" aria-hidden="true"></div>
    <div class="brand-name">The Lanternwrights</div>
    <div class="brand-tagline">We make it work, always !</div>

    <div class="holder">
      <div class="holder__name">Rosalind Kettering</div>
      <div class="holder__role">Partner</div>
    </div>

    <address class="contact">
      48 Thornapple Lane<br>
      Marlowe Springs, OH 45871<br>
      Cell : 267-555-0148<br>
      Email : rosalind.k.kettering@thelanternwrights.net<br>
      Web : www.thelanternwrights.net
    </address>
  </section>

  <section class="card card--back">
    <div class="brand-mark" aria-hidden="true"></div>
    <div class="web">www.thelanternwrights.net</div>
  </section>
</main>
</body>
</html>
```